Emergency Management Consulting Flyer

Company name: Stone Harbor Emergency Management

I am looking for a postcard design for my emergency management consulting business. I'm looking for something that has some colors and is double sided, on side with the information on services provided and the other side with the contact information. For the main side I'm looking for the following:

How prepared are you?

Services Provided:
Healthcare Preparedness
EOC Support
Emergency Planning
Mitigation Planning
Business Continuity
Disaster Response
Training and Exercises
Project Management
And more

Affordable for small and large organizations
Stand-by contracts available

On the back side, I'm looking for Contact Us section.

Overall I'm looking for something a bit more modern and need to have at least one disaster photo. If you have questions please message me.

Target Market(s)

Government, Healthcare Facilities, Businesses

Industry/Entity Type

Consulting

Requirements
Must have
• Disaster Picture, modern looking
• For the main side I'm looking for the following:
• How prepared are you?
• Services Provided:
• Healthcare Preparedness
• EOC Support
• Emergency Planning
• Mitigation Planning
• Business Continuity
• Disaster Response
• Training and Exercises
• Project Management
• And more
• Affordable for small and large organizations
• Stand-by contracts available

```html
<!DOCTYPE html>
<html lang="en">
<head>
<meta charset="utf-8">
<title>Stone Harbor Emergency Management – Postcard</title>
<link rel="stylesheet" href="https://fonts.googleapis.com/css2?family=Comfortaa:wght@400;600&family=Noto+Serif&family=Oswald:wght@500;700&family=Open+Sans:ital,wght@0,300;0,400;0,700;1,700&display=swap">
<style>
  :root {
    --backdrop: #4a2a08;
    --sky-top: #2f5f73;
    --sky-bottom: #dfe6ef;
    --yellow: #f6d716;
    --gold: #f2b81a;
    --ink: #1f1f1f;
    --orange: #f08a24;
    --red: #e53b2c;
    --blue: #1677c4;
    --navy: #2a3e8e;
    --paper: #ececec;
    --white: #ffffff;
  }
  * { box-sizing: border-box; margin: 0; padding: 0; }
  html, body { width: 801px; height: 1200px; overflow: hidden; }
  body { background: var(--backdrop); position: relative; font-family: "Open Sans", sans-serif; }

  .card { position: absolute; left: 42px; width: 711px; height: 550px; box-shadow: 4px 6px 10px rgba(0,0,0,.5); overflow: hidden; }
  .card--front { top: 44px; background: linear-gradient(180deg, var(--sky-top) 0%, #6f95a6 35%, #b9c8d6 62%, var(--sky-bottom) 100%); }
  .card--back { top: 614px; background: var(--paper); }

  .team-photo { position: absolute; z-index: 1; left: 330px; top: 32px; width: 372px; height: 300px; border-radius: 40% 40% 20% 20%; background: radial-gradient(ellipse at 55% 50%, #8a8e96 0%, #5b6068 50%, rgba(91,96,104,0) 72%); }
  .headline { position: absolute; z-index: 2; left: 30px; top: 34px; font-family: "Comfortaa", sans-serif; font-weight: 600; font-size: 50px; line-height: 60px; color: var(--yellow); text-shadow: 1px 2px 3px rgba(0,0,0,.35); white-space: nowrap; }
  .services-title { position: absolute; left: 32px; top: 208px; font-family: "Open Sans", sans-serif; font-weight: 400; font-size: 21px; color: var(--gold); letter-spacing: .3px; text-shadow: 1px 1px 2px rgba(0,0,0,.3); }
  .services { position: absolute; left: 32px; top: 249px; list-style: none; }
  .services li { font-family: "Noto Serif", serif; font-size: 19px; line-height: 30.6px; color: var(--ink); padding-left: 30px; position: relative; }
  .services li::before { content: ""; position: absolute; left: 1px; top: 8px; width: 15px; height: 15px; border-radius: 50%; background: radial-gradient(circle at 40% 35%, #ffd35a, var(--orange) 60%, #b85d10); box-shadow: 0 0 0 2px rgba(255,255,255,.6); }

  .offer-box { position: absolute; z-index: 2; left: 358px; top: 339px; width: 314px; height: 96px; border-radius: 4px; background: linear-gradient(90deg, var(--orange), var(--red)); display: flex; align-items: center; justify-content: center; text-align: center; font-family: "Oswald", sans-serif; font-weight: 500; font-size: 21px; line-height: 26px; color: var(--white); text-shadow: 1px 1px 2px rgba(0,0,0,.35); }
  .brand-box { position: absolute; z-index: 2; left: 358px; top: 442px; width: 314px; height: 82px; border-radius: 4px; background: var(--white); box-shadow: 1px 2px 4px rgba(0,0,0,.35); display: flex; align-items: center; gap: 10px; padding-left: 14px; }
  .brand-mark { width: 18px; height: 18px; border-radius: 50%; background: var(--orange); flex: none; }
  .brand-name { font-family: "Open Sans", sans-serif; font-weight: 700; font-size: 17px; line-height: 21px; color: #2b2b2b; }

  .office-photo { position: absolute; left: 26px; top: 16px; width: 496px; height: 154px; background: linear-gradient(90deg, #3d4a4c 0%, #8c9a98 35%, #d6dcdc 70%, #eef1f1 100%); }
  .photo-frame { position: absolute; left: 26px; top: 16px; width: 508px; height: 158px; background: #d9d9d9; }
  .brand-tag { position: absolute; left: 32px; top: 22px; width: 172px; height: 40px; background: var(--white); display: flex; align-items: center; gap: 6px; padding-left: 6px; }
  .brand-tag .brand-mark { width: 12px; height: 12px; }
  .brand-tag .brand-name { font-size: 10px; line-height: 12px; }

  .mail-area { position: absolute; background: var(--white); font-family: Arial, sans-serif; font-size: 19px; color: #000; text-align: center; }
  .mail-area--postage { left: 534px; top: 16px; width: 158px; height: 158px; padding-top: 54px; line-height: 26px; }
  .mail-area--address { left: 344px; top: 174px; width: 348px; height: 276px; padding-top: 46px; }
  .mail-area--barcode { left: 90px; top: 454px; width: 602px; height: 62px; padding-top: 18px; }
  .address-back { position: absolute; left: 26px; top: 174px; width: 318px; height: 276px; background: #dcdcdc; }

  .contact { position: absolute; left: 28px; top: 176px; width: 303px; }
  .contact__offer { height: 124px; background: var(--blue); color: var(--white); font-weight: 300; font-size: 21.5px; line-height: 30px; text-align: center; display: flex; align-items: center; justify-content: center; }
  .contact__band { height: 36px; background: linear-gradient(90deg, var(--orange), var(--red)); color: var(--white); font-weight: 700; font-size: 13px; display: flex; align-items: center; justify-content: center; text-shadow: 1px 1px 1px rgba(0,0,0,.3); }
  .contact__details { height: 108px; background: linear-gradient(180deg, #2258b0, var(--navy)); color: var(--white); padding: 14px 0 0 15px; }
  .contact__phone { font-family: "Oswald", sans-serif; font-weight: 700; font-size: 35px; line-height: 44px; letter-spacing: .5px; }
  .contact__address { font-style: italic; font-weight: 700; font-size: 15.5px; line-height: 22px; }
</style>
</head>
<body>
  <section class="card card--front">
    <div class="team-photo" role="img" aria-label="Photo of a smiling business team giving thumbs up"></div>
    <h1 class="headline">How prepared<br>are you?</h1>
    <h2 class="services-title">SERVICES PROVIDED:</h2>
    <ul class="services">
      <li>Healthcare Preparedness</li>
      <li>EOC Support</li>
      <li>Emergency Planning</li>
      <li>Mitigation Planning</li>
      <li>Business Continuity</li>
      <li>Disaster Response</li>
      <li>Training and Exercises</li>
      <li>Project Management</li>
      <li>And more</li>
    </ul>
    <div class="offer-box">Affordable for small<br>and large organizations<br>Stand-by contracts available</div>
    <div class="brand-box">
      <span class="brand-mark"></span>
      <span class="brand-name">STONE HARBOR<br>EMERGENCY MANAGEMENT</span>
    </div>
  </section>

  <section class="card card--back">
    <div class="photo-frame"></div>
    <div class="office-photo" role="img" aria-label="Photo of two business professionals in a modern glass office building"></div>
    <div class="brand-tag">
      <span class="brand-mark"></span>
      <span class="brand-name">STONE HARBOR<br>EMERGENCY MANAGEMENT</span>
    </div>
    <div class="mail-area mail-area--postage">Postage<br>Area</div>
    <div class="address-back"></div>
    <div class="mail-area mail-area--address">Address Area</div>
    <div class="contact">
      <div class="contact__offer">Affordable for small<br>and large organizations<br>Stand-by contracts available</div>
      <div class="contact__band">Stone Harbor Emergency Management</div>
      <div class="contact__details">
        <div class="contact__phone">Call: 01234 56789</div>
        <div class="contact__address">Suite 00, Cityname, Countyname</div>
      </div>
    </div>
    <div class="mail-area mail-area--barcode">Barcode Area</div>
  </section>
</body>
</html>
```